Business Card Design Project

Need a business card designed for a horse racing/gambling centered company.
Company name is BrightQuill.com.au
Company colours are similar to those in the logo.
Something clean and modern , designer given liberty to be creative.
Incorporate the logo is preferred.
Single or Double Sided fine
Must include :
Name
Mobile Number
Email Address
Reason: Apologies, I have been traveling unexpectedly with business and just need the extra two days to reply and give feedback before making a decision.
Industry/Entity Type
Business

```html
<!DOCTYPE html>
<html lang="en">
<head>
<meta charset="utf-8">
<title>BrightQuill.com.au Business Card</title>
<link rel="stylesheet" href="https://fonts.googleapis.com/css2?family=Oswald:wght@500&family=Roboto:wght@700&display=swap">
<style>
  :root {
    --bg: #eef1f1;
    --white: #ffffff;
    --green: #1ec27a;
    --green-deep: #14a866;
    --ink: #1c1c1c;
    --card-dark: #262626;
  }
  * { box-sizing: border-box; margin: 0; padding: 0; }
  html, body { width: 1200px; height: 900px; overflow: hidden; }
  body {
    background: var(--bg);
    position: relative;
    font-family: "Roboto", Arial, sans-serif;
  }
  .card {
    position: absolute;
    width: 344px;
    height: 600px;
    border-radius: 28px;
    overflow: hidden;
  }
  .card--front { left: 247px; top: 160px; background: var(--white); }
  .card--back { left: 670px; top: 152px; background: var(--card-dark); }

  .brand {
    position: absolute;
    left: 50%;
    transform: translateX(-50%);
    border-radius: 50%;
    border: 6px solid var(--green);
    display: flex;
    align-items: center;
    justify-content: center;
    text-align: center;
  }
  .brand__name {
    font-family: "Roboto", Arial, sans-serif;
    font-weight: 700;
    color: var(--green);
    line-height: 1.15;
  }
  .card--front .brand { top: 22px; width: 180px; height: 180px; background: var(--white); }
  .card--front .brand__name { font-size: 20px; }
  .card--back .brand { top: 182px; width: 238px; height: 238px; background: var(--white); }
  .card--back .brand__name { font-size: 26px; }

  .name-band {
    position: absolute;
    left: 0; top: 263px;
    width: 100%; height: 100px;
    background: var(--ink);
    border-top: 7px solid var(--green);
    box-shadow: inset 0 3px 0 var(--white);
    display: flex; align-items: center; justify-content: center;
  }
  .name-band::after {
    content: "";
    position: absolute; left: 0; bottom: 0;
    width: 100%; height: 4px; background: var(--white);
  }
  .holder-name {
    font-family: "Oswald", "Arial Narrow", sans-serif;
    font-weight: 500;
    font-size: 40px;
    color: var(--white);
    letter-spacing: 0.5px;
    text-transform: uppercase;
  }
  .contact {
    position: absolute;
    left: 0; top: 363px;
    width: 100%; height: 237px;
    background: var(--green);
    list-style: none;
    padding: 42px 0 0 33px;
  }
  .contact__item {
    display: flex; align-items: center;
    height: 43px;
    color: var(--white);
    font-size: 17.5px;
    font-weight: 700;
  }
  .contact__icon { width: 19px; height: 19px; margin-right: 10px; flex: none; }
</style>
</head>
<body>
  <section class="card card--front">
    <div class="brand"><span class="brand__name">BrightQuill<br>.com.au</span></div>
    <div class="name-band"><h1 class="holder-name">Mara Ellison</h1></div>
    <ul class="contact">
      <li class="contact__item">
        <svg class="contact__icon" viewBox="0 0 24 24" fill="#fff"><path d="M6.6 10.8a15.1 15.1 0 0 0 6.6 6.6l2.2-2.2c.3-.3.7-.4 1-.2 1.1.4 2.3.6 3.6.6.6 0 1 .4 1 1V20c0 .6-.4 1-1 1A17 17 0 0 1 3 4c0-.6.4-1 1-1h3.5c.6 0 1 .4 1 1 0 1.3.2 2.5.6 3.6.1.3 0 .7-.2 1z"/></svg>
        +(041) 555 0187
      </li>
      <li class="contact__item">
        <svg class="contact__icon" viewBox="0 0 24 24"><rect x="2" y="5" width="20" height="14" fill="#fff"/><path d="M2 5l10 8 10-8" fill="none" stroke="#1ec27a" stroke-width="1.8"/></svg>
        mara@brightquill.com.au
      </li>
      <li class="contact__item">
        <svg class="contact__icon" viewBox="0 0 24 24" fill="none" stroke="#fff" stroke-width="1.8"><circle cx="12" cy="12" r="10"/><ellipse cx="12" cy="12" rx="4.5" ry="10"/><path d="M2 12h20M4 7h16M4 17h16"/></svg>
        www.brightquill.com.au
      </li>
    </ul>
  </section>

  <section class="card card--back">
    <div class="brand"><span class="brand__name">BrightQuill<br>.com.au</span></div>
  </section>
</body>
</html>
```